Business Card and Letterhead Design for Public Accounting Firm

Business card and letterhead design for a CPA Firm located in Orange County, CA. We're looking for a modern and professional design utilizing our existing logo. We'd like a clean "less is more" look, but also something that catches the eye. We provide a high level of service to our clients. Open to single or double sided business cards.

Additional info: color numbers on logo
Blue :
R 0
G 83
B 125

#00537D

Silver :

R 154
G 154
B 154

#9A9A9A

Target Market(s)

Businesses and individuals

Industry/Entity Type

Accounting

Contact Information for Business Card

Moss Whitfield & Danby LLP - 4827 Larkspur Vale Road, Irvine, CA 92614 - (949)731-2864 - mwdaccts.example

Font styles to use
Serif
Sans Serif
Other font styles liked:
• See font file uploaded

Colors
0054AA
0677BA
7BADD7
CADEEF
E8F1F8

Requirements
Nice to have
• Possibly use the font file provided which matches our logo, but adjust to be not in all caps

```html
<!DOCTYPE html>
<html lang="en">
<head>
<meta charset="utf-8">
<title>Moss Whitfield &amp; Danby LLP — Business Card</title>
<link rel="stylesheet" href="https://fonts.googleapis.com/css2?family=Cinzel:wght@400&family=Gelasio:wght@400&family=Arimo:wght@400&display=swap">
<style>
  :root {
    --backdrop: #cbd0d3;
    --card-white: #ffffff;
    --card-white-shade: #e9e9eb;
    --brand-blue: #00537d;
    --brand-silver: #9a9a9a;
    --ghost-blue: #1e5a85;
    --text-on-blue: #ffffff;
  }
  * { margin: 0; padding: 0; box-sizing: border-box; }
  html, body {
    width: 1200px; height: 1200px; overflow: hidden;
    background: var(--backdrop);
  }
  .canvas { position: relative; width: 1200px; height: 1200px; }

  .card {
    position: absolute;
    left: 250px;
    width: 700px;
    height: 400px;
    overflow: hidden;
  }

  /* Front */
  .card-front {
    top: 147px;
    background: linear-gradient(110deg, var(--card-white) 12%, var(--card-white-shade) 100%);
  }
  .front-lockup {
    position: absolute;
    inset: 0;
    display: flex;
    align-items: center;
    justify-content: center;
    gap: 18px;
  }
  .lockup-square {
    width: 14px; height: 14px;
    background: var(--brand-silver);
  }
  .firm-name {
    font-family: "Cinzel", "Times New Roman", serif;
    font-weight: 400;
    font-size: 24px;
    line-height: 1.1;
    letter-spacing: 0.12em;
    color: var(--brand-silver);
    text-transform: uppercase;
  }

  /* Back */
  .card-back {
    top: 652px;
    background: var(--brand-blue);
    color: var(--text-on-blue);
  }
  .contact {
    position: absolute;
    left: 59px;
    top: 53px;
    z-index: 1;
  }
  .person-name {
    font-family: "Gelasio", Georgia, serif;
    font-size: 29px;
    line-height: 1;
    font-weight: 400;
  }
  .person-role {
    font-family: "Arimo", Arial, sans-serif;
    font-size: 15.5px;
    margin-top: 4px;
  }
  .details {
    font-family: "Arimo", Arial, sans-serif;
    font-size: 11.5px;
    line-height: 18px;
    margin-top: 22px;
  }
  .details .web { margin-top: 20px; }
  .ghost-initials {
    position: absolute;
    right: 2px;
    bottom: -36px;
    font-family: "Gelasio", Georgia, serif;
    font-size: 176px;
    line-height: 1;
    letter-spacing: -0.06em;
    color: var(--ghost-blue);
    white-space: nowrap;
  }
</style>
</head>
<body>
<main class="canvas">
  <section class="card card-front" aria-label="Card front">
    <div class="front-lockup">
      <span class="lockup-square" aria-hidden="true"></span>
      <p class="firm-name">Moss Whitfield<br>&amp; Danby LLP</p>
    </div>
  </section>

  <section class="card card-back" aria-label="Card back">
    <div class="ghost-initials" aria-hidden="true">MW&amp;D</div>
    <div class="contact">
      <h1 class="person-name">Adrian Moss</h1>
      <p class="person-role">Founder</p>
      <div class="details">
        <p>4827 Larkspur Vale Road, Irvine, CA 92614</p>
        <p>(949)731-2864</p>
        <p class="web">www.mwdaccts.example</p>
      </div>
    </div>
  </section>
</main>
</body>
</html>
```